wine label

Label for wine, in black and silver, format to be in PDF ,EPS, PSD Label to be split main label to have Name: Morbray Ash family crest, dry grown, and Clare Valley
other section to have the type of wine ie: Grenache and year of harvest.
Some ideas we had our enclosed

```html
<!DOCTYPE html>
<html lang="en">
<head>
<meta charset="utf-8">
<title>Morbray Ash Wine Label</title>
<link rel="stylesheet" href="https://fonts.googleapis.com/css2?family=Grand+Hotel&family=Arimo:wght@400;700&display=swap">
<style>
  :root {
    --page: #ffffff;
    --ink: #111111;
    --silver-light: #e2e2e2;
    --silver-mid: #b9b9b9;
    --silver-dark: #7f7f7f;
  }
  html, body {
    margin: 0;
    padding: 0;
    overflow: hidden;
  }
  body {
    width: 896px;
    height: 1200px;
    background: var(--page);
    position: relative;
  }
  .label {
    position: absolute;
    left: 68px;
    width: 760px;
    background:
      linear-gradient(180deg, rgba(255,255,255,0.25) 0%, rgba(255,255,255,0) 35%, rgba(0,0,0,0.12) 100%),
      linear-gradient(90deg, var(--silver-mid) 0%, var(--silver-light) 30%, var(--silver-mid) 65%, var(--silver-dark) 100%);
    color: var(--ink);
  }
  .label--main {
    top: 200px;
    height: 414px;
  }
  .label--variety {
    top: 759px;
    height: 217px;
  }
  .crest-mark {
    position: absolute;
    left: 42px;
    top: 46px;
    width: 232px;
    height: 232px;
  }
  .brand {
    position: absolute;
    right: 52px;
    top: 92px;
    text-align: right;
  }
  .brand__name {
    margin: 0;
    font-family: "Grand Hotel", cursive;
    font-weight: 400;
    font-size: 90px;
    line-height: 1;
  }
  .brand__region {
    margin: 34px 0 0;
    font-family: "Arimo", sans-serif;
    font-weight: 700;
    font-size: 20px;
    line-height: 1;
    letter-spacing: 0.5px;
  }
  .variety__title {
    position: absolute;
    left: 0;
    right: 0;
    top: 52px;
    margin: 0;
    text-align: center;
    font-family: "Grand Hotel", cursive;
    font-weight: 400;
    font-size: 48px;
    line-height: 1;
  }
  .variety__rule {
    position: absolute;
    left: 41px;
    right: 41px;
    top: 136px;
    height: 3px;
    background: var(--ink);
  }
  .variety__abv {
    position: absolute;
    left: 0;
    right: 0;
    top: 170px;
    margin: 0;
    text-align: center;
    font-family: "Arimo", sans-serif;
    font-size: 19px;
    letter-spacing: 0.5px;
  }
</style>
</head>
<body>
  <section class="label label--main">
    <svg class="crest-mark" viewBox="0 0 232 232" aria-hidden="true">
      <circle cx="116" cy="116" r="110" fill="none" stroke="var(--ink)" stroke-width="8"/>
    </svg>
    <div class="brand">
      <h1 class="brand__name">Morbray Ash</h1>
      <p class="brand__region">DRY GROWN • CLARE VALLEY</p>
    </div>
  </section>

  <section class="label label--variety">
    <h2 class="variety__title">Old Man Grenache 2012</h2>
    <div class="variety__rule"></div>
    <p class="variety__abv">ALCOHOL 16%</p>
  </section>
</body>
</html>
```